No Credit Score QT and ZMR

I'm looking for a banner to display on emails as well as facebook. The facebook banner would need to be square and the other size is 728 x 90. We are a mortgage company that does mostly Military home loans. We would like to start out with just this banner, then do about 20 others once we find the right designer. I need something simple but that stands out. Our company website is www.harborpeakfinancial.com. The text for this will be ( Ask about our "No Credit Score" program for ZMR and QT)

```html
<!DOCTYPE html>
<html lang="en">
<head>
<meta charset="utf-8">
<title>No Credit Score – QT and ZMR Banners</title>
<link href="https://fonts.googleapis.com/css2?family=Montserrat:wght@700;900&family=Open+Sans:wght@700&display=swap" rel="stylesheet">
<style>
  :root {
    --stage: #0a0d30;
    --navy: #202768;
    --navy-deep: #2b3280;
    --red: #cc1b31;
    --white: #ffffff;
    --gold: #f2a019;
    --photo-light: #d9dbe0;
    --photo-mid: #9a9e97;
    --photo-dark: #5b5f58;
  }
  * { margin: 0; padding: 0; box-sizing: border-box; }
  html, body { width: 1200px; height: 1200px; overflow: hidden; background: var(--stage); }
  .canvas { position: relative; width: 1200px; height: 1200px; }

  .leaderboard { position: absolute; left: 309px; top: 177px; width: 582px; height: 72px; background: var(--navy); overflow: hidden; }
  .square-ad { position: absolute; left: 310px; top: 270px; width: 580px; height: 580px; background: var(--navy); overflow: hidden; }
  .art { position: absolute; inset: 0; width: 100%; height: 100%; }

  .headline { font-family: "Montserrat", sans-serif; font-weight: 900; color: var(--red); letter-spacing: 0.5px; white-space: nowrap; }
  .loan-label { font-family: "Montserrat", sans-serif; font-weight: 700; color: var(--white); line-height: 1.1; }
  .call-now { font-family: "Open Sans", sans-serif; font-weight: 700; color: var(--white); white-space: nowrap; }

  /* leaderboard */
  .leaderboard .call-now { position: absolute; left: 230px; top: 15px; width: 120px; text-align: center; font-size: 15px; line-height: 20px; letter-spacing: 0.5px; }
  .leaderboard .headline { position: absolute; left: 387px; top: 6px; font-size: 17.5px; }
  .leaderboard .loan-row { position: absolute; left: 398px; top: 36px; height: 24px; display: flex; align-items: center; }
  .leaderboard .loan-label { font-size: 9.5px; }
  .leaderboard .mark-square { width: 18px; height: 18px; background: var(--gold); margin-left: 5px; }
  .leaderboard .divider { width: 1px; height: 20px; background: #4a5193; margin: 0 13px; }
  .leaderboard .mark-circle { width: 22px; height: 22px; border-radius: 50%; background: var(--red); border: 2px solid var(--white); margin-right: 6px; }

  /* square */
  .square-ad .headline { position: absolute; left: 0; right: 0; top: 52px; text-align: center; font-size: 39px; }
  .square-ad .loan-row { position: absolute; left: 0; right: 0; top: 118px; height: 52px; display: flex; justify-content: center; align-items: center; }
  .square-ad .loan-label { font-size: 20px; }
  .square-ad .loan-zmr { text-align: right; }
  .square-ad .mark-square { width: 44px; height: 44px; background: var(--gold); margin-left: 10px; }
  .square-ad .divider { width: 1px; height: 44px; background: #4a5193; margin: 0 28px; }
  .square-ad .mark-circle { width: 48px; height: 48px; border-radius: 50%; background: var(--red); border: 3px solid var(--white); margin-right: 12px; }
  .square-ad .cta-band { position: absolute; left: 0; right: 0; bottom: 0; height: 58px; background: var(--red); display: flex; align-items: center; justify-content: center; }
  .square-ad .call-now { font-size: 25px; letter-spacing: 0.6px; }
</style>
</head>
<body>
<main class="canvas">

  <section class="leaderboard" aria-label="728 by 90 email banner">
    <svg class="art" viewBox="0 0 582 72" aria-hidden="false">
      <defs>
        <linearGradient id="photoSmall" x1="0" y1="0" x2="0" y2="1">
          <stop offset="0" stop-color="var(--photo-light)"/>
          <stop offset="1" stop-color="var(--photo-mid)"/>
        </linearGradient>
      </defs>
      <polygon points="0,30 30,0 0,0" fill="var(--navy-deep)"/>
      <polygon points="0,72 65,0 180,0 247,72" fill="var(--white)"/>
      <g role="img" aria-label="Photo of a soldier holding a model house in front of a flag">
        <polygon points="40,72 92,0 182,0 220,72" fill="url(#photoSmall)"/>
      </g>
      <polygon points="180,0 325,0 386,72 247,72" fill="var(--red)"/>
      <path d="M369,71 l3,-6 l6,-3 l-6,-3 l-3,-6 l-3,6 l-6,3 l6,3z" fill="var(--white)"/>
      <path d="M19,15 l1,-3 l3,-1 l-3,-1 l-1,-3 l-1,3 l-3,1 l3,1z" fill="var(--white)"/>
      <path d="M368,19 l1,-3 l3,-1 l-3,-1 l-1,-3 l-1,3 l-3,1 l3,1z" fill="var(--white)"/>
      <path d="M574,40 l1,-3 l3,-1 l-3,-1 l-1,-3 l-1,3 l-3,1 l3,1z" fill="var(--white)"/>
    </svg>
    <p class="call-now">Call Now<br>555-014-2290</p>
    <h2 class="headline">NO CREDIT SCORE</h2>
    <div class="loan-row">
      <span class="loan-label">&nbsp;ZMR<br>LOANS</span>
      <span class="mark-square"></span>
      <span class="divider"></span>
      <span class="mark-circle"></span>
      <span class="loan-label">QT<br>LOANS</span>
    </div>
  </section>

  <section class="square-ad" aria-label="Square social banner">
    <svg class="art" viewBox="0 0 580 580">
      <defs>
        <linearGradient id="photoLarge" x1="0" y1="0" x2="0" y2="1">
          <stop offset="0" stop-color="var(--photo-light)"/>
          <stop offset="0.6" stop-color="var(--photo-mid)"/>
          <stop offset="1" stop-color="var(--photo-dark)"/>
        </linearGradient>
      </defs>
      <polygon points="0,400 290,184 580,410 580,580 0,580" fill="var(--navy-deep)"/>
      <polygon points="0,462 290,184 580,474 580,580 0,580" fill="var(--white)"/>
      <g role="img" aria-label="Photo of a soldier in camouflage holding a model house, with an American flag behind">
        <polygon points="22,522 290,266 562,522" fill="url(#photoLarge)"/>
      </g>
      <path d="M542,372 l4,-9 l9,-4 l-9,-4 l-4,-9 l-4,9 l-9,4 l9,4z" fill="var(--white)"/>
    </svg>
    <h1 class="headline">NO CREDIT SCORE</h1>
    <div class="loan-row">
      <span class="loan-label loan-zmr">ZMR<br>LOANS</span>
      <span class="mark-square"></span>
      <span class="divider"></span>
      <span class="mark-circle"></span>
      <span class="loan-label">QT<br>LOANS</span>
    </div>
    <div class="cta-band"><p class="call-now">Call Now 555-014-2290</p></div>
  </section>

</main>
</body>
</html>
```